Business card with logo for a family psychologist

I need a business card for my private practice in the urban Chicago area as a psychologist. I see families and individuals who are going through difficult times - divorce, separation, illness, or trauma. I want to project hopefulness, competence, and caring.

Target Market(s)

Adults, other professionals - such as physicans and lawyers

Industry/Entity Type

Health Care

Contact Information for Business Card

Front should have my name and credentials; back should have location information including my email, phone

Font styles to use
Serif
Decorative
Script

Requirements
Must have
• Unique logo
Should not have
• No pictures or icons of people; no black

```html
<!DOCTYPE html>
<html lang="en">
<head>
<meta charset="utf-8">
<title>Laura Dixon, Ph.D. — Business Card</title>
<link href="https://fonts.googleapis.com/css2?family=Fjalla+One&family=Lato:wght@400&family=Caladea:wght@400&display=swap" rel="stylesheet">
<style>
  :root {
    --backdrop: #e9e6e2;
    --card-dark: #323439;
    --card-light: #ffffff;
    --accent: #f07f35;
    --ink-light: #ffffff;
    --ink-grey: #5a5a5c;
    --rule-grey: #c9c9c9;
  }
  * { margin: 0; padding: 0; box-sizing: border-box; }
  html, body { width: 1200px; height: 1000px; overflow: hidden; }
  body { background: var(--backdrop); position: relative; }

  .card {
    position: absolute;
    left: 284px;
    width: 625px;
    height: 357px;
    border-radius: 22px;
    box-shadow: 0 6px 18px rgba(0,0,0,0.18);
  }
  .card--front { top: 141px; background: var(--card-dark); }
  .card--back { top: 532px; background: var(--card-light); }

  /* Front */
  .front-rule-top {
    position: absolute; left: 132px; top: 138px;
    width: 361px; height: 1px; background: var(--ink-light);
  }
  .front-marker { position: absolute; left: 308px; top: 131px; }
  .front-name {
    position: absolute; left: 0; width: 100%; top: 155px;
    text-align: center;
    font-family: "Fjalla One", sans-serif;
    font-weight: 400;
    font-size: 41px; letter-spacing: 1.5px;
    color: var(--ink-light); line-height: 1;
  }
  .front-title-row {
    position: absolute; left: 132px; top: 205px; width: 361px;
    display: flex; align-items: center; gap: 12px;
  }
  .front-title-row .rule { flex: 1; height: 1px; background: var(--ink-light); }
  .front-title {
    font-family: "Lato", sans-serif; font-size: 15.5px;
    color: var(--ink-light); white-space: nowrap;
  }

  /* Back */
  .back-identity {
    position: absolute; right: 330px; top: 153px; text-align: right;
  }
  .back-name {
    font-family: "Fjalla One", sans-serif; font-size: 26px;
    color: var(--accent); line-height: 1.1; letter-spacing: 0.3px;
  }
  .back-title {
    font-family: "Caladea", serif; font-size: 14.5px;
    color: var(--ink-grey); line-height: 1.2; letter-spacing: 0.3px;
    margin-top: 2px;
  }
  .back-divider {
    position: absolute; left: 312px; top: 148px;
    width: 1px; height: 62px; background: var(--rule-grey);
  }
  .contact-list {
    position: absolute; left: 331px; top: 141px; list-style: none;
    font-family: "Caladea", serif; font-size: 14.5px;
    color: var(--ink-grey); line-height: 18.5px; letter-spacing: 0.3px;
  }
  .contact-list li { display: flex; align-items: flex-start; }
  .contact-list .icon { width: 17px; flex: none; display: flex; align-items: center; height: 18.5px; }
  .contact-list .indent { padding-left: 17px; }
</style>
</head>
<body>

<section class="card card--front" aria-label="Card front">
  <div class="front-rule-top"></div>
  <svg class="front-marker" width="10" height="20" viewBox="0 0 10 20" aria-hidden="true">
    <polygon points="0,0 10,0 10,15 5,20 0,15" fill="var(--accent)"/>
  </svg>
  <h1 class="front-name">LAURA DIXON, PH.D.</h1>
  <div class="front-title-row">
    <span class="rule"></span>
    <span class="front-title">Licensed Clinical Psychologist</span>
    <span class="rule"></span>
  </div>
</section>

<section class="card card--back" aria-label="Card back">
  <div class="back-identity">
    <p class="back-name">Laura Dixon, Ph.D.</p>
    <p class="back-title">Licensed Clinical Psychologist</p>
  </div>
  <div class="back-divider"></div>
  <ul class="contact-list">
    <li>
      <span class="icon"><svg width="11" height="14" viewBox="0 0 11 14" aria-hidden="true"><path d="M5.5 0C2.5 0 0 2.3 0 5.3 0 9 5.5 14 5.5 14S11 9 11 5.3C11 2.3 8.5 0 5.5 0Zm0 7.4a2.1 2.1 0 1 1 0-4.2 2.1 2.1 0 0 1 0 4.2Z" fill="var(--accent)"/></svg></span>
      <span>240 W. Harlow Suite 910</span>
    </li>
    <li class="indent">Chicago, Illinois 60611</li>
    <li>
      <span class="icon"><svg width="12" height="10" viewBox="0 0 12 10" aria-hidden="true"><path d="M0 3.2C0 1.2 2.7 0 6 0s6 1.2 6 3.2V4H9V2.8H3V4H0Z M1.5 5h9l1 5H.5Z" fill="var(--accent)"/><circle cx="6" cy="7.3" r="1.3" fill="#fff"/></svg></span>
      <span>312-555-0148</span>
    </li>
    <li>
      <span class="icon"><svg width="12" height="9" viewBox="0 0 12 9" aria-hidden="true"><rect width="12" height="9" fill="var(--accent)"/><path d="M0 0 6 5 12 0" stroke="#fff" stroke-width="1.2" fill="none"/></svg></span>
      <span>Drlauraedixon@mailhub.com</span>
    </li>
  </ul>
</section>

</body>
</html>
```